Creative & Professional Business Card for hair salon

We are looking to update our business cards. Our salon is creative, modern, progressive and professional and looking for a design that will reflect this.

```html
<!DOCTYPE html>
<html lang="en">
<head>
<meta charset="utf-8">
<title>Driftwood Hair – Business Card</title>
<link rel="stylesheet" href="https://fonts.googleapis.com/css2?family=Ubuntu:wght@300;400&display=swap">
<style>
  :root {
    --page: #ffffff;
    --frame: #d9d9d9;
    --charcoal-top: #363b39;
    --charcoal-bottom: #050505;
    --salon-orange: #f26522;
    --orange-glow: #f58220;
    --ink: #1b1b1b;
    --rule: #5a5a5a;
  }
  * { box-sizing: border-box; margin: 0; padding: 0; }
  html, body {
    width: 934px; height: 1200px; overflow: hidden;
    background: var(--page);
    font-family: "Ubuntu", sans-serif;
  }
  .sheet { position: relative; width: 934px; height: 1200px; }
  .side-panel {
    position: absolute; left: 0; width: 934px;
    border: 1px solid var(--frame); background: var(--page);
  }
  .side-panel--front { top: 0; height: 534px; }
  .side-panel--back { top: 664px; height: 536px; }

  .card { position: absolute; width: 830px; height: 434px; }
  .card--front {
    left: 57px; top: 56px;
    background: radial-gradient(ellipse 90% 95% at 50% 0%, var(--charcoal-top) 0%, #1a1c1b 55%, var(--charcoal-bottom) 100%);
  }
  .card--back {
    left: 54px; top: 46px;
    background: radial-gradient(ellipse 70% 80% at 100% 100%, var(--orange-glow) 0%, var(--salon-orange) 55%),
                var(--salon-orange);
  }

  .brand {
    position: absolute; display: flex; align-items: center; gap: 12px;
    font-weight: 300; white-space: nowrap;
  }
  .brand__dot { border-radius: 50%; flex: none; }
  .brand--front {
    left: 0; right: 0; top: 188px; justify-content: center;
    color: var(--salon-orange); font-size: 46px;
  }
  .brand--front .brand__dot { width: 30px; height: 30px; background: var(--salon-orange); }
  .brand--back {
    left: 38px; top: 153px; color: var(--ink); font-size: 29px; gap: 9px;
  }
  .brand--back .brand__dot { width: 20px; height: 20px; background: var(--ink); }

  .divider {
    position: absolute; left: 339px; top: 81px; height: 184px;
    border-left: 2px dashed var(--ink);
  }

  .contact-list { position: absolute; left: 372px; top: 78px; list-style: none; }
  .contact-list__item {
    display: flex; align-items: center; height: 41px;
    font-size: 19px; color: var(--ink); letter-spacing: 0.2px;
  }
  .contact-list__item--small { font-size: 17px; letter-spacing: -0.2px; }
  .contact-list__icon { width: 20px; height: 20px; margin-right: 23px; flex: none; }

  .appointment {
    position: absolute; left: 38px; top: 322px;
    font-size: 19px; color: var(--ink);
  }
  .write-line { position: absolute; height: 0; border-top: 1px solid var(--rule); }
  .write-line--first { left: 283px; width: 516px; top: 340px; }
  .write-line--second { left: 38px; width: 761px; top: 392px; }
</style>
</head>
<body>
<div class="sheet">

  <section class="side-panel side-panel--front">
    <div class="card card--front">
      <div class="brand brand--front">
        <span class="brand__dot"></span>
        <span class="brand__name">Driftwood Hair</span>
      </div>
    </div>
  </section>

  <section class="side-panel side-panel--back">
    <div class="card card--back">
      <div class="brand brand--back">
        <span class="brand__dot"></span>
        <span class="brand__name">Driftwood Hair</span>
      </div>

      <div class="divider"></div>

      <ul class="contact-list">
        <li class="contact-list__item">
          <svg class="contact-list__icon" viewBox="0 0 20 20" aria-hidden="true">
            <path d="M5 17c-1-3 0-8 4-11l2-1 1 3-2 1.5c-1.5 1.5-2 3.5-1.5 5l2 .2 .5 3-3 .8z" fill="#1b1b1b"/>
          </svg>
          <span>0755501234</span>
        </li>
        <li class="contact-list__item">
          <svg class="contact-list__icon" viewBox="0 0 20 20" aria-hidden="true">
            <circle cx="10" cy="10" r="8" fill="none" stroke="#1b1b1b" stroke-width="2.4"/>
            <circle cx="10" cy="10" r="3.2" fill="none" stroke="#1b1b1b" stroke-width="2.4"/>
            <path d="M13.2 7v5c0 2 3 2 4.5 0" fill="none" stroke="#1b1b1b" stroke-width="2.4"/>
          </svg>
          <span>salon@driftwoodhair.com</span>
        </li>
        <li class="contact-list__item">
          <svg class="contact-list__icon" viewBox="0 0 20 20" aria-hidden="true">
            <path d="M10 2 1.5 10H4v7h4.5v-5h3v5H16v-7h2.5z" fill="#1b1b1b"/>
          </svg>
          <span>5/12 Harbour Lane, Coastview</span>
        </li>
        <li class="contact-list__item">
          <svg class="contact-list__icon" viewBox="0 0 20 20" aria-hidden="true">
            <g fill="none" stroke="#1b1b1b" stroke-width="1.6">
              <circle cx="10" cy="10" r="8.5"/>
              <ellipse cx="10" cy="10" rx="3.8" ry="8.5"/>
              <path d="M1.5 10h17M3 5.5h14M3 14.5h14"/>
            </g>
          </svg>
          <span>www.driftwoodhair.com.au</span>
        </li>
        <li class="contact-list__item contact-list__item--small">
          <svg class="contact-list__icon" viewBox="0 0 20 20" aria-hidden="true">
            <rect x="1.5" y="1.5" width="17" height="17" rx="2" fill="#1b1b1b"/>
          </svg>
          <span>www.friendspage.com/DriftwoodHairbyJoMarlow</span>
        </li>
      </ul>

      <p class="appointment">Your next appointment is :</p>
      <div class="write-line write-line--first"></div>
      <div class="write-line write-line--second"></div>
    </div>
  </section>

</div>
</body>
</html>
```